Electrical company needs a brochure designed for electrical construction work

we need a brochure designed for our company BRONZEWAY ELECTRICAL INSTALLATIONS. we are a group of electricians working in the construction industry delivering electrical constructon services to builders and other clients in the commercial and Industrial working environments. we would like our logo to stand out with a dark theme and also give a professional fee.l we have a brief description of what we do and our experiences in a word doc i will provide it along with our logo design

Target Market(s)

builders for commercial and industrial construction projects

Industry/Entity Type

Electric Company

Font styles to use
Serif

Colors
0456a4
96b7d9
5c5c5c
757575
000000
aaaaaa
ec1f27
33a6d7
0493ce

Requirements
Must have
• a professional feel,
Nice to have
• some wording that makes us stand out and brings all the attention

```html
<!DOCTYPE html>
<html lang="en">
<head>
<meta charset="utf-8">
<title>Bronzeway Electrical Installations – Brochure Spread</title>
<link rel="stylesheet" href="https://fonts.googleapis.com/css2?family=Montserrat:wght@400;500;600;700&display=swap">
<style>
  :root {
    --stage: #d9dadc;
    --navy-deep: #1c1e2e;
    --navy: #23263d;
    --navy-glow: #2d4a8a;
    --band-blue: #0553a8;
    --band-line: #0a62bf;
    --footer-dark: #1e1f27;
    --text-light: #e6e9f2;
    --accent-red: #ec1f27;
    --accent-cyan: #33a6d7;
    --illus-blue: #0493ce;
    --illus-green: #3aa657;
  }
  * { margin: 0; padding: 0; box-sizing: border-box; }
  html, body {
    width: 1200px; height: 1200px; overflow: hidden;
    background: var(--stage);
    font-family: "Montserrat", sans-serif;
  }
  .spread {
    position: absolute; left: 0; top: 212px;
    width: 1200px; height: 775px;
    display: flex;
  }
  .page { position: relative; width: 600px; height: 775px; overflow: hidden; }

  /* Left page */
  .page-left {
    background: linear-gradient(90deg, var(--navy-deep) 0%, var(--navy) 60%, var(--navy-glow) 100%);
  }
  .illustration { position: absolute; border-radius: 6px; }
  .illustration-tools {
    left: 41px; top: 38px; width: 516px; height: 232px;
    background: radial-gradient(ellipse at 55% 55%, rgba(4,147,206,.45), rgba(58,166,87,.18) 45%, rgba(35,38,61,0) 75%);
  }
  .illustration-fixtures {
    left: 300px; top: 580px; width: 257px; height: 140px;
    background: radial-gradient(ellipse at 50% 55%, rgba(58,166,87,.45), rgba(200,205,215,.15) 50%, rgba(35,38,61,0) 78%);
  }
  .intro-copy {
    position: absolute; left: 43px; top: 283px; width: 514px;
    color: var(--text-light); font-size: 10.1px; line-height: 17.7px;
    text-align: justify;
  }
  .intro-copy p { margin-bottom: 11.5px; }
  .intro-copy p.safety { width: 353px; margin-top: 18px; }

  /* Right page */
  .page-right { background: var(--navy); }
  .letter {
    position: absolute; left: 53px; top: 104px; width: 494px;
    color: var(--text-light); font-size: 10.1px; line-height: 17.7px;
    text-align: justify;
  }
  .project-band {
    position: absolute; left: 0; top: 279px; width: 600px; height: 358px;
    background: var(--band-blue);
  }
  .band-artwork {
    position: absolute; left: 294px; top: 30px; width: 280px; height: 290px;
    border-radius: 50%;
    background: radial-gradient(circle, rgba(10,98,191,.9), rgba(5,83,168,0) 70%);
  }
  .project-list {
    position: absolute; left: 52px; top: 30px;
    list-style: none; color: var(--text-light);
    font-size: 10.3px; line-height: 19.2px;
  }
  .project-list li { position: relative; padding-left: 11px; }
  .project-list li::before {
    content: ""; position: absolute; left: 0; top: 8px;
    width: 4px; height: 4px; border-radius: 50%; background: var(--accent-red);
  }
  .page-footer {
    position: absolute; left: 0; top: 637px; width: 600px; height: 138px;
    background: var(--footer-dark);
  }
  .tagline {
    position: absolute; left: 69px; top: 43px;
    color: #fff; font-size: 17px; line-height: 19.5px; font-weight: 400;
  }
  .tagline strong { font-weight: 700; }
  .brand {
    position: absolute; left: 378px; top: 58px;
    display: flex; align-items: center; gap: 8px;
  }
  .brand-dot { width: 20px; height: 20px; border-radius: 50%; background: var(--accent-cyan); flex: none; }
  .brand-name {
    color: var(--accent-cyan); font-size: 10.5px; font-weight: 700;
    line-height: 13px; letter-spacing: .3px; white-space: nowrap;
  }
</style>
</head>
<body>
  <main class="spread">
    <section class="page page-left">
      <div class="illustration illustration-tools" role="img" aria-label="Flat illustration of an electrician in a green hard hat surrounded by multimeters, gloves, pliers, tape and power meters"></div>
      <div class="intro-copy">
        <p>Electrical contracting company able to perform a great variety of electrical work required, recent experience on heavy industrial electrical installs involving complex systems on gas plant, 5 years total. Commercial and industrial situations are something we have always been exposed to and have been involved in many large construction jobs around Harrowvale.</p>
        <p>We are a small company just getting started and have been operating part time for over a year working late nights after our day jobs, working most weekends Saturday and Sundays, working towards building our company to be able to work full time and grow our business to something we can be proud of.</p>
        <p>Recently the opportunity arose that we could move away from our employment and take the business to a new level and work full time with 100% commitment we believe that our drive and passion for our trade and industry separates us from the unwilling and we will push ourselves to the limit to achieve and exceed any expectations that are placed upon us.</p>
        <p class="safety">Our background in large commercial and industrial construction jobs around Harrowvale has granted us the ability to introduce and implement stringent safety practices, we will always encourage and drive safety to the best of our ability to mitigate risk or harm to any person, not just because of our duty of care but because we like to see potential work colleagues/employees go home safely to their families unharmed.</p>
      </div>
      <div class="illustration illustration-fixtures" role="img" aria-label="Flat illustration of a cable reel, light bulbs, power board, battery and wall sockets"></div>
    </section>

    <section class="page page-right">
      <div class="letter">
        <p>Hi,</p>
        <p>I'm Dean Whitcombe a local electrician in Harrowvale running a small electrical contracting company Bronzeway Electrical Installations. If you are in need of reliable, punctual, and experienced electricians to work in with your company then please give me a call I'm happy to discuss my business or submit a quote for any work you may have available. I have a lot of experience in the local construction industry I have worked on a lot of commercial and industrial construction jobs around Harrowvale for at least the last 10 years some jobs include.</p>
      </div>

      <div class="project-band">
        <div class="band-artwork" role="img" aria-label="Line-art icons of a light bulb, plug, ruler, pencil, battery, house and voltmeter"></div>
        <ul class="project-list">
          <li>Ridgeview high school</li>
          <li>St Brennan catholic college</li>
          <li>Underground cabling on many subdivisions including Fernlea, Ashcombe, Tallowby</li>
          <li>Deskline Supplies</li>
          <li>Northgate substation HV switch gear</li>
          <li>Redgum substation HV switch gear</li>
          <li>The Harrowvale harbourside wave pool etc</li>
          <li>Cobble point receiving station project</li>
          <li>Kestrel barracks single leap project</li>
          <li>Civic assembly house multiple contracts</li>
          <li>The Harrowvale events centre</li>
          <li>Air base runway lighting</li>
          <li>Harrowvale regional airport multiple different contracts</li>
          <li>Harrowvale general hospital oncology building</li>
          <li>Harrowvale general hospital multiple various maintenance contracts</li>
          <li>Harrowvale correctional facility</li>
        </ul>
      </div>

      <footer class="page-footer">
        <p class="tagline">The Best<br><strong>Electrical contractor</strong><br>in the city</p>
        <div class="brand">
          <span class="brand-dot"></span>
          <span class="brand-name">BRONZEWAY<br>ELECTRICAL INSTALLATIONS</span>
        </div>
      </footer>
    </section>
  </main>
</body>
</html>
```